Meridel Physical Therapy Co Brochure

We need a brochure that underscores the advantages of our PT clinic. The brochure will be a 6 X 9 postcard (cardboard paper). We like the use of bullet points (since physicians have limited time), underscore our location, provide an introduction to our clinic, create a nice logo, and what separates us (see below). Most important is location, about us (separates us from competition), and the logo.

Please make sure to list our website as www.meridel-pt.example. Also include schedule your Physical Therapy session at www.meridel-pt.example or call 555-214-0386.

What Makes Us Different

One-on-One Treatments
Our commitment to you is that you will receive one-on-one attention from one of our staff members with a Doctorate of Physical Therapy. We will never double, triple, or quadruple book "your appointment slot." This ensures that you get one-on-one time with your Doctor of Physical Therapy, and you are not doing your exercises alone in the corner like at the hospital or at the corporate physical therapy clinics. If you are currently seeing a Physical Therapist that is leaving you alone to perform your exercises, to go and treat other patients or is double / triple booking your appointment, please give us call today!

State-of the-Art Equipment
Even though we are a small / local PT clinic, we still made the capital investment to have only the best equipment for you to use in our clinic. Our Doctor of Physical Therapy will guide you through an individually customized plan on treatment, based on your initial evaluation. Thereafter, we will provide Home Exercises that will normally be different than your clinic treatment program. If your current clinic is simply having you perform the Home Exercises in the clinic, please give us a call today!

Russian Speaking
We are one of the few Russian-speaking Physical Therapy clinics in the Chicagoland area. If Russian is your preferred language, please give us a call today!

Manual Therapy
We believe that manual therapy is an important element towards rehabilitation for many patients. Our doctors are highly trained in the approaches of manual therapy. If your current clinic does not believe in manual therapy, please give us a call today!

Friendly and Caring Staff

Flexible Hours

Convenient Location
Located at the corner of Tollamere Rd and Brenwick Rd, in the same shopping plaza as the Silver Mist Auto Spa and the Glazewell Bakes. We are directly across the street from the NHKA of Harlow Springs.

What We Do
Diagnoses We Treat

At Meridel Physical Therapy, we treat a variety of diagnoses. Here is a list of some of the typical things we treat:

Neck and Back Pain
Shoulder Pain/Rotator Cuff Disorders/Bursitis
Hip Pain
Knee, Ankle, and Foot Pain/Sprains
Post-Operative Care for Orthopedic Surgery including Total Joint Replacement and Spine Surgery
Balance Deficits/Fall Prevention
General Strengthening
Tendinitis
Specialty Programs

Work Injury
Sports Medicine/Sports Performance
Motor Vehicle Accident/Whiplash
Post-Surgical Protocols

Welcome to
Meridel Physical Therapy Company
Meridel Physical Therapy will utilize both physical therapy and group strength and balance classes to achieve an effective long-term, meaningful lifestyle change toward renewed strength and active living. Our patients will follow a three-step system, which begins with the Physical Therapist initial evaluation, continues into a rehabilitative stage, and terminates with a personalized ongoing lifestyle wellness plan.

Our goal is to help our patients improve function, independence, and the quality of their life. We believe that age is just a number, and it does not define one’s ability. We want to encourage everyone to invest the time to increase their strength, physical activity level, and the quality of their body movements.
We are one of the few Russian-speaking Physical Therapy clinics in Chicagoland area. Doctors of Physical Therapy at Meridel Physical Therapy Co are dedicated to developing a treatment plan that is custom-designed and tailored to each patient’s pace and comfort level.

Location
2247 Brenwick Rd
Harlow Springs, IL 60412
Phone: (555) 214-0386
Fax: (555) 906-3417

Physical Therapists Owned and Managed clinic

Target Market(s)

geriatrics, orthopedic / sports medicine, and work / auto accident injury patients

Industry/Entity Type

Physical Therapy

Font styles to use
Serif

Requirements
Must have
• location of our clinic
• logo of our clinic
• Schedule an a session online via our website (www.meridel-pt.example) or by via
• phone 555 214 0386
• link to our temporary website - http://2736.rehabsitetmp.example/ (do not list it on the brochure)
Nice to have
• could mention that we will have outstanding equipment (Vorla-trek machine, Brawnmax total gym system, Pulsevane Modalities, etc)
Should not have
• should be able to fit nicely on 6 X 9 Postcard (needs to be double sided!)

```html
<!DOCTYPE html>
<html lang="en">
<head>
<meta charset="utf-8">
<title>Meridel Physical Therapy Co — About Us</title>
<link href="https://fonts.googleapis.com/css2?family=Delius&family=Montserrat:wght@800&family=Nunito:wght@900&display=swap" rel="stylesheet">
<style>
  :root {
    --brand-blue: #416eb4;
    --brand-green: #b5cc5e;
    --brand-green-pale: #dfe9bd;
    --paper: #ffffff;
    --photo-light: #eef1f3;
    --photo-mid: #d9e0e4;
    --photo-teal: #a9dade;
    --photo-skin: #e9c6ad;
    --text-light: #ffffff;
  }
  * { margin: 0; padding: 0; box-sizing: border-box; }
  html, body {
    width: 1200px; height: 800px; overflow: hidden; background: var(--paper);
  }
  .postcard {
    position: relative; width: 1200px; height: 800px; overflow: hidden;
    background: var(--paper);
  }
  .hero-photo {
    position: absolute; left: 382px; top: 0; width: 818px; height: 260px;
    background:
      radial-gradient(ellipse 180px 90px at 430px 150px, var(--photo-teal) 0%, rgba(169,218,222,0) 100%),
      radial-gradient(ellipse 140px 70px at 640px 150px, var(--photo-skin) 0%, rgba(233,198,173,0) 100%),
      linear-gradient(90deg, rgba(255,255,255,1) 0%, var(--photo-light) 30%, var(--photo-mid) 70%, var(--photo-light) 100%);
  }
  .movement-figures {
    position: absolute; left: 158px; top: 120px; width: 302px; height: 645px;
  }
  .figures-upper {
    position: absolute; left: 0; top: 0; width: 302px; height: 420px;
    border-radius: 140px 0 0 60px;
    background: linear-gradient(90deg, rgba(223,233,189,0.6) 0%, var(--brand-green-pale) 35%, var(--brand-green) 65%, var(--brand-blue) 100%);
  }
  .figures-lower {
    position: absolute; left: 212px; top: 420px; width: 90px; height: 225px;
    border-radius: 0 0 0 30px;
    background: linear-gradient(90deg, var(--brand-green) 0%, var(--brand-green) 50%, var(--brand-blue) 100%);
  }
  .logo {
    position: absolute; left: 36px; top: 66px; display: flex; align-items: center; gap: 14px;
  }
  .logo-mark {
    width: 56px; height: 56px; border-radius: 50%; background: var(--brand-green); flex: none;
  }
  .logo-name {
    font-family: "Nunito", sans-serif; font-weight: 900; font-size: 28px; line-height: 32px;
    color: var(--brand-blue);
  }
  .about-panel {
    position: absolute; left: 432px; top: 260px; width: 768px; height: 540px;
    background: var(--brand-blue);
  }
  .about-title {
    position: absolute; left: 496px; top: 280px;
    font-family: "Montserrat", sans-serif; font-weight: 800; font-size: 46px; letter-spacing: 2px;
    line-height: 56px; color: var(--text-light);
  }
  .about-column {
    position: absolute; top: 340px;
    font-family: "Delius", sans-serif; font-size: 18.6px; line-height: 26.7px;
    color: var(--text-light);
  }
  .about-column p + p { margin-top: 26.7px; }
  .column-left { left: 495px; width: 330px; }
  .column-right { left: 843px; width: 340px; }
  .contact {
    position: absolute; left: 37px; top: 640px; font-style: normal;
    font-family: "Nunito", sans-serif; font-weight: 900; color: var(--brand-blue);
  }
  .contact-address { font-size: 24px; line-height: 28px; }
  .contact-phone { font-size: 24px; line-height: 30px; margin-top: 8px; }
  .contact-web { font-size: 22px; line-height: 28px; }
</style>
</head>
<body>
<main class="postcard">
  <div class="hero-photo" role="img" aria-label="Photograph of a physical therapist guiding a patient's leg through a knee stretch"></div>
  <div class="movement-figures" role="img" aria-label="Illustration of three silhouetted figures rising from a bend to standing, in green and blue">
    <div class="figures-upper"></div>
    <div class="figures-lower"></div>
  </div>

  <div class="logo">
    <span class="logo-mark"></span>
    <span class="logo-name">Meridel Physical<br>Therapy Co</span>
  </div>

  <div class="about-panel"></div>
  <h1 class="about-title">ABOUT US</h1>

  <div class="about-column column-left">
    <p>Meridel Physical Therapy will<br>utilize both physical therapy and<br>group strength and balance classes<br>to achieve an effective long-term,<br>meaningful lifestyle change toward<br>renewed strength and active living.<br>Our patients will follow a three-<br>step system, which begins with the<br>Physical Therapist initial evaluation,<br>continues into a rehabilitative stage,<br>and terminates with a personalized<br>ongoing lifestyle wellness plan.</p>
    <p>Our goal is to help our patients<br>improve function, independence, and<br>the quality of their life. We believe</p>
  </div>

  <div class="about-column column-right">
    <p>that age is just a number, and it does<br>not define one’s ability. We want to<br>encourage everyone to invest the time<br>to increase their strength, physical<br>activity level, and the quality of their<br>body movements.</p>
    <p>We are one of the few Russian-<br>speaking Physical Therapy clinics in<br>Chicagoland area. Doctors of Physical<br>Therapy at Meridel Physical Therapy<br>Co are dedicated to developing a<br>treatment plan that is custom-<br>designed and tailored to each patient’s<br>pace and comfort level.</p>
  </div>

  <address class="contact">
    <div class="contact-address">2247 Brenwick Rd<br>Harlow Springs, IL 60412</div>
    <div class="contact-phone">(555) 214 0386</div>
    <div class="contact-web">www.meridel-pt.example</div>
  </address>
</main>
</body>
</html>
```